IT Services Business Card Design

We require a business card design for an IT services company called RT Code Transit.

We specialize in taking an organisations software and readying it for deployment to new environments (e.g. Nex 3 to Nex 5). This process is termed application packaging. This is not the same as putting things in boxes but I am happy to use boxes as a pun icon ;-) This is our second step in branding, we currently have a new logo and our poor excuse of a website is next to be updated but it contains information on who we are and what we cover at rtcodetransit.example

We are looking for a fun, modern but stylish and professional looking design.

I have attached the logo in multiple formats including vector formats (and the fonts that created the logo if required)
Updates

Thanks to all the designers so far, some great designs in there.  I will be selecting a card design on the deadline date. 

However, there is still time to submit some more designs.  The majority of the ones I have so far are typical simplistic designs that we have all seen before and I have enough of those to choose from now.  If you wish to submit any more designs, please submit somthing unusual to grab our attention.

Target Market(s)

Project executives of large organisations looking for Nexora migrations

Industry/Entity Type

Software

Requirements
Must have
• Want to show company name, contact name, title, main number, contact number, fax number, email address and website address. I do not want to show the address.
Must use the attached logo, retaining the colours in them.

This has to be a double-sided design. I will be using pelby.example and will be selecting their rounded corner business card design.

Their templates and design requirements (sizing etc.) can be found here: http://uk.pelby.example/help/faq/templates-and-guidelines.html

Happy for company name or website to be on either side of the card.

This design has to be original and not used before for another company

Would like to style it around the business colours in the logo
Nice to have
• Pelby.example has an option for multiple card designs to appear on the back. If this is possible in the budget and time you have and you have a design(s) that work with that but carry the same style and theme, that would be nice to see but not necessary.
Should not have
• We do not want to put a postal address on the cards

```html
<!DOCTYPE html>
<html lang="en">
<head>
<meta charset="utf-8">
<title>RT Code Transit – Business Card</title>
<link rel="stylesheet" href="https://fonts.googleapis.com/css2?family=Arimo:wght@400;700&family=Jost:wght@300;400&display=swap">
<style>
  :root {
    --page-bg: #ecebe8;
    --card-bg: #ffffff;
    --brand-blue: #3b73dc;
    --rule-grey: #6b625b;
    --logo-grey: #6b625b;
    --text-dark: #1d1d1d;
    --card-shadow: rgba(0, 0, 0, 0.18);
  }
  * { box-sizing: border-box; margin: 0; padding: 0; }
  html, body {
    width: 1200px;
    height: 868px;
    overflow: hidden;
    background: var(--page-bg);
  }
  .canvas {
    position: relative;
    width: 1200px;
    height: 868px;
  }
  .card {
    position: absolute;
    width: 520px;
    height: 330px;
    background: var(--card-bg);
    border-radius: 30px;
    overflow: hidden;
    box-shadow: 0 6px 20px var(--card-shadow);
  }
  .card--front { left: 60px; top: 150px; }
  .card--back  { left: 620px; top: 390px; }

  /* Front bands */
  .band {
    position: absolute;
    left: 0;
    width: 100%;
    background: var(--brand-blue);
    color: #fff;
    display: flex;
    align-items: center;
    justify-content: center;
  }
  .band--top { top: 0; height: 48px; }
  .band--bottom { bottom: 0; height: 46px; }
  .rule {
    position: absolute;
    left: 0;
    width: 100%;
    height: 3px;
    background: var(--rule-grey);
  }
  .rule--top { top: 52px; }
  .rule--bottom { bottom: 50px; }

  .holder-name {
    font-family: "Arimo", Arial, sans-serif;
    font-weight: 700;
    font-size: 21px;
    letter-spacing: -0.2px;
  }
  .holder-title {
    font-family: "Arimo", Arial, sans-serif;
    font-weight: 400;
    font-size: 14px;
    margin-left: 5px;
    position: relative;
    top: -3px;
  }
  .website {
    font-family: "Jost", "Century Gothic", sans-serif;
    font-weight: 400;
    font-size: 15px;
    letter-spacing: 3.2px;
  }

  /* Logo lockup */
  .brand-lockup {
    position: absolute;
    display: flex;
    align-items: center;
    gap: 14px;
  }
  .brand-lockup--front { left: 66px; top: 102px; }
  .brand-lockup--back  { left: 62px; top: 110px; }
  .brand-mark {
    width: 54px;
    height: 54px;
    border-radius: 50%;
    background: var(--brand-blue);
    flex: none;
  }
  .brand-name {
    font-family: "Jost", "Century Gothic", sans-serif;
    font-weight: 300;
    font-size: 46px;
    color: var(--logo-grey);
    letter-spacing: 0.5px;
    white-space: nowrap;
  }

  /* Contact block */
  .contacts {
    position: absolute;
    left: 0;
    width: 100%;
    top: 195px;
    font-family: "Arimo", Arial, sans-serif;
    font-size: 14.5px;
    color: var(--text-dark);
    text-align: center;
  }
  .contact-row {
    display: flex;
    justify-content: center;
    gap: 14px;
    margin-bottom: 8px;
  }
  .contact-item {
    display: inline-flex;
    align-items: center;
    gap: 5px;
  }
  .contact-icon {
    width: 12px;
    height: 12px;
    fill: var(--brand-blue);
  }

  .back-website {
    position: absolute;
    left: 0;
    width: 100%;
    bottom: 48px;
    text-align: center;
    font-family: "Jost", "Century Gothic", sans-serif;
    font-size: 16px;
    letter-spacing: 3.4px;
    color: var(--text-dark);
  }
</style>
</head>
<body>
<main class="canvas">

  <section class="card card--front" aria-label="Business card front">
    <header class="band band--top">
      <span class="holder-name">Your Name,</span><span class="holder-title">Title</span>
    </header>
    <div class="rule rule--top"></div>

    <div class="brand-lockup brand-lockup--front">
      <span class="brand-name">RT Code Transit</span>
      <span class="brand-mark"></span>
    </div>

    <div class="contacts">
      <div class="contact-row">
        <span class="contact-item">
          <svg class="contact-icon" viewBox="0 0 12 12" aria-hidden="true"><path d="M2.5 0.5 L4.5 0.5 L5 3 L3.6 4 C4.3 5.7 6.3 7.7 8 8.4 L9 7 L11.5 7.5 L11.5 9.5 C11.5 10.8 10.6 11.5 9.5 11.5 C4.7 11.2 0.8 7.3 0.5 2.5 C0.5 1.4 1.2 0.5 2.5 0.5 Z"/></svg>
          0123 456789
        </span>
        <span class="contact-item">
          <svg class="contact-icon" viewBox="0 0 12 12" aria-hidden="true"><path d="M3.5 0 H8.5 A1 1 0 0 1 9.5 1 V11 A1 1 0 0 1 8.5 12 H3.5 A1 1 0 0 1 2.5 11 V1 A1 1 0 0 1 3.5 0 Z M4 1.5 V8 H8 V1.5 Z"/></svg>
          0123 456789
        </span>
        <span class="contact-item">
          <svg class="contact-icon" viewBox="0 0 12 12" aria-hidden="true"><path d="M3 1 H9 V4 H11 A1 1 0 0 1 12 5 V10 A1 1 0 0 1 11 11 H1 A1 1 0 0 1 0 10 V5 A1 1 0 0 1 1 4 H3 Z M4 2 V5 H8 V2 Z"/></svg>
          0123 456789
        </span>
      </div>
      <div class="contact-row">
        <span class="contact-item">
          <svg class="contact-icon" viewBox="0 0 12 12" aria-hidden="true"><path d="M0 2.5 H12 V10 H0 Z M0.8 3.2 L6 7 L11.2 3.2 Z" fill-rule="evenodd"/></svg>
          info@rtcodetransit.example
        </span>
      </div>
    </div>

    <div class="rule rule--bottom"></div>
    <footer class="band band--bottom">
      <span class="website">www.rtcodetransit.example</span>
    </footer>
  </section>

  <section class="card card--back" aria-label="Business card back">
    <div class="brand-lockup brand-lockup--back">
      <span class="brand-name">RT Code Transit</span>
      <span class="brand-mark"></span>
    </div>
    <p class="back-website">www.rtcodetransit.example</p>
  </section>

</main>
</body>
</html>
```